Business card for auto dealership

Looking for a clean modern design.
Would like attached logo incorporated

Industry/Entity Type

Car dealership

Contact Information for Business Card

Name, website, phone, cell, fax, email

```html
<!DOCTYPE html>
<html lang="en">
<head>
<meta charset="utf-8">
<title>Harlow Truck &amp; Auto — Business Card</title>
<link rel="stylesheet" href="https://fonts.googleapis.com/css2?family=Inter:wght@300;400;700;800&display=swap">
<style>
  :root {
    --canvas: #e9e9e9;
    --ink: #000000;
    --paper: #ffffff;
    --stripe-light: #f1f1f1;
    --stripe-dark: #141414;
  }
  * { margin: 0; padding: 0; box-sizing: border-box; }
  html, body { width: 1200px; height: 1200px; overflow: hidden; }
  body {
    background: var(--canvas);
    font-family: "Inter", sans-serif;
    position: relative;
  }
  .card {
    position: absolute;
    width: 800px;
    height: 457px;
    overflow: hidden;
    box-shadow: 0 6px 18px rgba(0,0,0,0.18);
  }
  /* Front */
  .card-front {
    left: 52px; top: 130px;
    background: linear-gradient(115deg, var(--paper) 0%, var(--stripe-light) 100%);
  }
  .front-panel { position: absolute; inset: 0; }
  .brand-name {
    position: absolute;
    font-weight: 800;
    letter-spacing: -0.5px;
    line-height: 1.1;
    text-align: center;
    white-space: nowrap;
  }
  .card-front .brand-name {
    left: 20px; top: 212px; width: 330px;
    font-size: 31px;
    color: var(--ink);
  }
  .holder { position: absolute; right: 24px; top: 92px; text-align: right; color: var(--paper); }
  .holder-name { font-size: 35px; font-weight: 800; letter-spacing: 0.3px; line-height: 1.1; }
  .holder-title { font-size: 26px; font-weight: 300; letter-spacing: 0.5px; margin-top: 4px; }
  .divider { position: absolute; left: 451px; top: 185px; width: 349px; height: 4px; }
  .contact-list { position: absolute; right: 22px; top: 212px; list-style: none; color: var(--paper); }
  .contact-item {
    display: flex; align-items: center; justify-content: flex-end;
    height: 40px; font-size: 20px; font-weight: 400; letter-spacing: 0.3px;
  }
  .contact-item svg { width: 22px; height: 22px; margin-left: 14px; flex: none; }
  /* Back */
  .card-back {
    left: 315px; top: 613px; width: 802px;
    background: linear-gradient(115deg, var(--ink) 0%, var(--stripe-dark) 50%, var(--ink) 100%);
  }
  .card-back .brand-name {
    left: 0; right: 0; top: 178px;
    font-size: 48px;
    color: var(--paper);
  }
  .back-url {
    position: absolute; left: 0; right: 0; top: 373px;
    text-align: center; color: var(--paper);
    font-size: 29px; font-weight: 400; letter-spacing: 0.5px;
  }
</style>
</head>
<body>

<section class="card card-front">
  <svg class="front-panel" width="800" height="457" viewBox="0 0 800 457" aria-hidden="true">
    <polygon points="468,0 800,0 800,457 303,457" fill="#000"/>
  </svg>
  <div class="brand-name">Harlow Truck &amp; Auto</div>

  <div class="holder">
    <div class="holder-name">JONATHAN DOE</div>
    <div class="holder-title">GENERAL MANAGER</div>
  </div>

  <svg class="divider" viewBox="0 0 349 4" aria-hidden="true">
    <line x1="0" y1="2" x2="92" y2="2" stroke="#fff" stroke-width="4" stroke-dasharray="1.5 2"/>
    <rect x="92" y="0" width="257" height="4" fill="#fff"/>
  </svg>

  <ul class="contact-list">
    <li class="contact-item">yourname@harlowauto.com
      <svg viewBox="0 0 24 24" fill="none" stroke="#fff" stroke-width="2"><rect x="3" y="5" width="18" height="14" rx="1"/><path d="M3 6l9 7 9-7"/></svg>
    </li>
    <li class="contact-item">+1 (555) 010-246
      <svg viewBox="0 0 24 24" fill="#fff"><path d="M6.6 10.8c1.4 2.8 3.8 5.1 6.6 6.6l2.2-2.2c.3-.3.7-.4 1-.2 1.1.4 2.3.6 3.6.6.6 0 1 .4 1 1V20c0 .6-.4 1-1 1C10.6 21 3 13.4 3 4c0-.6.4-1 1-1h3.5c.6 0 1 .4 1 1 0 1.3.2 2.5.6 3.6.1.3 0 .7-.2 1l-2.3 2.2z"/></svg>
    </li>
    <li class="contact-item">+1 (555) 013-5790
      <svg viewBox="0 0 24 24" fill="#fff"><rect x="3" y="8" width="5" height="14" rx="1"/><path d="M10 2h8v6h3v14H10z"/><g fill="#000"><rect x="12" y="11" width="2" height="2"/><rect x="16" y="11" width="2" height="2"/><rect x="12" y="15" width="2" height="2"/><rect x="16" y="15" width="2" height="2"/><rect x="12" y="4" width="4" height="3"/></g></svg>
    </li>
    <li class="contact-item">0800 5550 2468
      <svg viewBox="0 0 24 24" fill="none" stroke="#fff" stroke-width="2"><rect x="6" y="2" width="12" height="20" rx="2"/><line x1="11" y1="18" x2="13" y2="18"/></svg>
    </li>
    <li class="contact-item">www.harlowauto.com
      <svg viewBox="0 0 24 24" fill="none" stroke="#fff" stroke-width="1.6"><circle cx="12" cy="12" r="10"/><ellipse cx="12" cy="12" rx="4.5" ry="10"/><line x1="2" y1="12" x2="22" y2="12"/><path d="M4 6.5h16M4 17.5h16"/></svg>
    </li>
  </ul>
</section>

<section class="card card-back">
  <div class="brand-name">Harlow Truck &amp; Auto</div>
  <div class="back-url">www.harlowauto.com</div>
</section>

</body>
</html>
```